Online Digital Solutions Agency needs a New Business Card

We are a Online/Digital solution agency. We provide WordPress Solutions, Online & Digital Marketing Solutions including SEO, Social Media Marketing and Managed Hosting including VPS and Cloud Hosting solutions. We also design and build bespoke web sites and web applications for various clients. We are very good at site migrations, 3rd party API integrations and mobile app development.

We are rebranding our agency and have already designed a new logo. We have selected 5-6 colours as our base colour and are currently building our new website based around these colour scheme.

Our logo indicates that we are a cloud solution providers, and (i.e. the Clouds), and developers (i.e. HTML Tags, and CSS formats). We use the 5-6 base colours and use various shades of these colours as required.

Our old website is located at: www.brambleforgelabs.com

And our new website is going to be at (we are working on it at the moment ...):
https://creative.brambleforgelabs.co.uk/

Our slogan is "Digital Transformation Specialist"

What we mean by that is; we can take any existing business and get them up and transform them in to the digital world, starting with Hosting, Web Design, Development & Online Marketing aspects.

The powerpoint is a document that we use to present our projects to clients at the moment, and the cloud is on the background as we clarified earlier. (Just to get the idea)

What we are looking for is a Great WoW factor design to start with, ideally with the Logo and Logo colour scheme if possible but not required as long as the designers can do better, and basically give life to our logo and company via the Business card design.

Ideally with some icons perhaps to indicate the address, location, mobile, email, and website would be good but again optional as long as there is a good design.

The cloud can be used as a background if required in a light shade or as a watermark share perhaps.

The logos' and the Illustrator files are shared with you so you can use them as required.

Ideally the business card should have a Name, title, Mobile, Email , Website, Address and perhaps some social media links.

Target Market(s)

New Startups, SME's, Contract and Outsource Clients

Contact Information for Business Card

Company Name:
==============
BrambleForge Labs (UK) Ltd.

Tag Line:
========
“Digital Transformation Specialists”

Adress:
=======

Suite KR73054
14-16 Ashgrove Lane
London
E9 4PD.

Name:
=====
Idris Malek

Title: (Optional)
=============
FQTA, PgD (RNOM)

Role:
=====
Digital Solutions Architect

Email:
=====
idris@brambleforgelabs.uk

WebSite:
=======
http://www.brambleforgelabs.uk

OR

www.brambleforgelabs.uk

Mobile:
======
0044 (0)75 218 30479

OR

+44 (0)75 218 30479

LinkedIN: (Optional)
========
https://uk.linkedin.com/in/idrismalek

Skype: (Optional)
======
idris.malek

Twitter (Optional) : idrismalek

Font styles to use
Serif
Sans Serif

Requirements
Must have
• The Logo
• Business Name
• Person Name
• Title
• Mobile
• Email
• Website
• Address
• I have provided the colour scheme on my files.
Nice to have
• Twiter
• Linked in
• Facebook

```html
<!DOCTYPE html>
<html lang="en">
<head>
<meta charset="utf-8">
<title>BrambleForge Labs – Business Card</title>
<link rel="stylesheet" href="https://fonts.googleapis.com/css2?family=Work+Sans:wght@400;500;600;700&display=swap">
<style>
  :root {
    --brand-blue: #1b63b5;
    --brand-blue-deep: #14529c;
    --brand-sky: #4aa6e0;
    --ink: #4d4f53;
    --paper: #ffffff;
    --stage: #e9ebee;
  }
  * { box-sizing: border-box; margin: 0; padding: 0; }
  html, body { width: 1200px; height: 930px; overflow: hidden; }
  body {
    background: var(--stage);
    font-family: "Work Sans", Arial, sans-serif;
    position: relative;
  }
  .card {
    position: absolute;
    width: 560px;
    height: 320px;
    border-radius: 4px;
    overflow: hidden;
    box-shadow: 0 10px 28px rgba(0,0,0,.18);
  }
  /* Front */
  .card-front {
    left: 70px; top: 80px;
    background: linear-gradient(135deg, var(--brand-blue) 0%, var(--brand-blue-deep) 100%);
    color: var(--paper);
  }
  .card-front .wordmark {
    position: absolute;
    left: 0; right: 0; top: 120px;
    text-align: center;
    font-size: 40px;
    font-weight: 700;
    color: var(--paper);
  }
  .card-front .tagline {
    position: absolute;
    left: 0; right: 0; bottom: 34px;
    text-align: center;
    font-size: 15px;
    letter-spacing: .06em;
    font-weight: 400;
  }
  /* Back */
  .card-back {
    left: 570px; top: 520px;
    background: var(--paper);
  }
  .card-back .wordmark {
    position: absolute;
    left: 22px; top: 130px;
    width: 230px;
    text-align: center;
    font-size: 27px;
    font-weight: 700;
    color: var(--brand-blue);
  }
  .card-back .divider {
    position: absolute;
    left: 262px; top: 40px;
    width: 2px; height: 190px;
    background: var(--brand-blue);
  }
  .details {
    position: absolute;
    left: 282px; top: 34px;
    color: var(--ink);
    font-size: 11.5px;
    line-height: 1.45;
  }
  .details .name {
    font-size: 22px;
    font-weight: 600;
    color: var(--brand-blue);
    letter-spacing: .02em;
    line-height: 1.1;
  }
  .details .credentials, .details .role { font-size: 11.5px; }
  .details .address { margin-top: 8px; }
  .contact { list-style: none; margin-top: 8px; }
  .contact li { display: flex; align-items: center; gap: 7px; }
  .contact svg { width: 10px; height: 10px; flex: none; fill: var(--brand-blue); }
  .contact .web strong { color: var(--brand-blue); font-weight: 600; }
  .wave { position: absolute; left: 0; bottom: 0; width: 560px; height: 150px; }
  .social {
    position: absolute;
    right: 40px; bottom: 60px;
    display: flex; align-items: center; gap: 7px;
    color: var(--paper);
    font-size: 12px;
    transform: rotate(-14deg);
    transform-origin: right center;
  }
  .social .dot { width: 9px; height: 9px; border-radius: 50%; background: var(--paper); }
</style>
</head>
<body>

<section class="card card-front" aria-label="Card front">
  <div class="wordmark">BrambleForge Labs</div>
  <div class="tagline">Digital Transformation Specialists</div>
</section>

<section class="card card-back" aria-label="Card back">
  <div class="wordmark">BrambleForge Labs</div>
  <div class="divider"></div>

  <div class="details">
    <div class="name">IDRIS MALEK</div>
    <div class="credentials">FQTA, PgD (RNOM)</div>
    <div class="role">Digital Solutions Architect</div>
    <div class="address">14-16, Ashgrove Lane London<br>E9 4PD United Kingdom</div>
    <ul class="contact">
      <li><svg viewBox="0 0 10 10"><path d="M2 0.5l1.8 2-1 1.2c.6 1.3 1.5 2.2 2.6 2.7l1.2-1 2 1.8-1.2 1.9C4.6 8.8 1.2 5.4.6 1.7z"/></svg>0044 (0)75 218 30479</li>
      <li><svg viewBox="0 0 10 10"><path d="M2.5 0h5v10h-5zM3.4 1v7h3.2V1z"/></svg>+44 (0)75 218 30479</li>
      <li><svg viewBox="0 0 10 10"><path d="M0 1.5h10v7H0zm1 1v.3l4 2.6 4-2.6v-.3zm0 1.5v3.5h8V4L5 6.6z"/></svg>idris@brambleforgelabs.uk</li>
      <li class="web"><svg viewBox="0 0 10 10"><circle cx="5" cy="5" r="4.5"/></svg>www.<strong>brambleforgelabs</strong>.uk</li>
    </ul>
  </div>

  <svg class="wave" viewBox="0 0 560 150" preserveAspectRatio="none" aria-hidden="true">
    <path d="M0 120 C150 150 260 60 400 45 C470 38 520 30 560 15 L560 150 L0 150Z" fill="var(--brand-sky)"/>
    <path d="M0 130 C150 160 260 72 400 57 C470 50 520 40 560 25 L560 150 L0 150Z" fill="var(--brand-blue)"/>
  </svg>
  <div class="social"><span class="dot"></span>idrismalek</div>
</section>

</body>
</html>
```